Redesign wellness clinic website

The project is redesign a wellness clinic http://www.thornleighvitality.example. The new website is to be responsive,clean,bright and a strong call to action which is to book an appointment. The logo will remain the same but the colour scheme on the website should be reflect purple white and green. I want it to be bright and cheerful and the feeling of clarity. The website shouldn't be overloaded with content but more visuals.

Target Market(s)

Anyone that has corporate wellness benefits within the downtown Toronto core. Majority of audience are professional working in Media, Telecommunications and Investments.

Industry/Entity Type

Health And Wellness

Number of Pages Required

5+ page

Font styles to use
Sans Serif

Colors
ffffff
886aae
acd036

Requirements
Must have
• -Strong call to action which is book an appointment like this page https://www.kestrelmotion.example/
• -Services provided icons on the page like https://www.brightpathvitalityhouse.example/
• - Pictures of a good visualizing a fit and healthy life
• - Strong ratings from Quorva, Zintrel, PostMaz, similar to this website http://www.summitbalancehealth.example/our-team-professionals/
• - Bright and clear
Should not have
• -No black and white images (redo our pictures)
• -Dark themes

```html
<!DOCTYPE html>
<html lang="en">
<head>
<meta charset="utf-8">
<title>Thornleigh Vitality Centre</title>
<link rel="stylesheet" href="https://fonts.googleapis.com/css2?family=Lato:ital,wght@0,400;0,700;1,400&family=Oswald:wght@300;400;500&display=swap">
<style>
:root{
  --purple:#886aae;
  --purple-deep:#6e4f96;
  --purple-soft:#efe7f3;
  --green:#acd036;
  --green-dark:#8fb126;
  --ink:#333333;
  --muted:#666666;
  --white:#ffffff;
  --footer:#323232;
  --footer-deep:#1f1f1f;
  --grey-band:#f1f1f1;
}
*{box-sizing:border-box;margin:0;padding:0}
html,body{width:1200px;height:4063px;overflow:hidden}
body{font-family:"Lato",Arial,sans-serif;color:var(--ink);background:var(--white);position:relative}
.icon-defs{position:absolute;width:0;height:0;overflow:hidden}
/* header */
.site-header{position:absolute;left:0;top:0;width:1200px;height:106px;background:var(--white)}
.brand{position:absolute;left:84px;top:16px;display:flex;align-items:center;gap:12px}
.brand-mark{width:64px;height:64px;border-radius:50%;border:5px solid var(--purple)}
.brand-name{font-weight:700;font-size:19px;color:var(--purple-deep);line-height:1.2}
.brand-name small{display:block;font-size:13px;color:var(--green-dark);font-weight:700}
.topbar{position:absolute;right:84px;top:15px;display:flex;gap:28px;font-size:12px;color:var(--muted);align-items:center}
.topbar span{display:flex;align-items:center;gap:6px}
.topbar svg{fill:var(--muted)}
.social{display:flex;gap:12px}
.social i{width:12px;height:12px;border-radius:50%;background:var(--green);display:block}
.topbar-rule{position:absolute;left:400px;right:84px;top:44px;border-top:1px solid #e4e4e4}
.main-nav{position:absolute;right:84px;top:64px;display:flex;gap:30px;font-size:14px;color:var(--ink)}
/* hero */
.hero{position:absolute;left:0;top:106px;width:1200px;height:625px;overflow:hidden}
.hero-photo{position:absolute;inset:0;background:
  radial-gradient(ellipse 420px 160px at 760px 520px,rgba(250,248,246,.95),rgba(250,248,246,0)),
  radial-gradient(ellipse 300px 260px at 360px 200px,rgba(120,128,118,.7),rgba(120,128,118,0)),
  radial-gradient(ellipse 260px 200px at 620px 330px,rgba(214,180,160,.75),rgba(214,180,160,0)),
  radial-gradient(ellipse 380px 300px at 1020px 180px,#f2efeb,rgba(242,239,235,0)),
  linear-gradient(100deg,#6e6862 0%,#9b938c 35%,#d4cdc6 62%,#c4bcb4 100%)}
.hero-shade{position:absolute;inset:0;background:linear-gradient(90deg,rgba(30,25,25,.5),rgba(30,25,25,.05) 55%,rgba(30,25,25,0))}
.hero-kicker{position:absolute;left:84px;top:210px;font-family:"Oswald",sans-serif;font-weight:300;font-size:30px;color:var(--white);letter-spacing:1px}
.hero-title{position:absolute;left:84px;top:245px;font-family:"Oswald",sans-serif;font-weight:400;font-size:48px;color:var(--white);letter-spacing:1px}
.btn-outline-light{position:absolute;left:84px;top:330px;height:56px;padding:0 20px;border:2px solid var(--white);color:var(--white);font-size:15px;display:flex;align-items:center;gap:8px;letter-spacing:.5px}
.hero-arrow{position:absolute;top:280px}
/* location */
.location{position:absolute;left:0;top:731px;width:1200px;height:204px;box-shadow:0 10px 18px rgba(0,0,0,.06)}
.location h2{position:absolute;left:84px;top:28px;font-size:38px;font-weight:700;color:var(--purple-deep)}
.location p{position:absolute;top:80px;font-size:18px;color:var(--ink)}
.btn-outline{position:absolute;left:84px;top:128px;height:42px;padding:0 16px;border:2px solid var(--purple);color:var(--purple-deep);font-size:13px;display:flex;align-items:center;gap:6px}
/* services */
.services{position:absolute;left:0;top:1010px;width:1200px;height:529px;overflow:hidden}
.services-photo{position:absolute;inset:0;background:
  radial-gradient(ellipse 260px 300px at 700px 200px,#d9c7de,rgba(217,199,222,0)),
  radial-gradient(ellipse 300px 200px at 420px 360px,#b79cc9,rgba(183,156,201,0)),
  radial-gradient(ellipse 260px 240px at 980px 120px,#e8dcea,rgba(232,220,234,0)),
  linear-gradient(90deg,#7d5fa1,#9c82b8 45%,#8a6cab)}
.services-tint{position:absolute;inset:0;background:rgba(136,106,174,.72)}
.section-title{position:absolute;left:0;width:1200px;text-align:center;font-family:"Oswald",sans-serif;font-weight:400;font-size:28px;letter-spacing:1px;display:flex;justify-content:center;align-items:center;gap:22px}
.section-title::before,.section-title::after{content:"";width:70px;border-top:1px solid currentColor;opacity:.6}
.services .section-title{top:36px;color:var(--white)}
.service{position:absolute;width:200px;text-align:center;color:var(--white);font-size:18px}
.service-icon{width:110px;height:110px;border-radius:50%;background:var(--green);margin:0 auto 14px;display:flex;align-items:center;justify-content:center;box-shadow:0 0 0 5px rgba(172,208,54,.35)}
.service-ring{width:86px;height:86px;border-radius:50%;border:3px solid var(--white);display:flex;align-items:center;justify-content:center}
.service-ring svg{width:52px;height:52px}
/* about */
.about-text{position:absolute;left:84px;top:1648px;width:500px}
.about-text h3{font-size:24px;font-weight:400;line-height:1.3;color:var(--ink)}
.about-text .sub{font-size:18px;color:var(--muted);margin-top:8px}
.about-text h4{font-size:22px;color:var(--green-dark);margin-top:26px;font-weight:700}
.about-text p{font-size:18px;color:var(--ink);line-height:1.35}
.about-text a{color:var(--purple-deep);text-decoration:none}
.video{position:absolute;left:612px;top:1612px;width:501px;height:317px;display:flex;align-items:center;justify-content:center;background:
  radial-gradient(ellipse 120px 160px at 80px 160px,#e9e2d0,rgba(233,226,208,0)),
  radial-gradient(ellipse 160px 140px at 260px 130px,#f4f1ee,rgba(244,241,238,0)),
  radial-gradient(ellipse 140px 180px at 440px 240px,#3f6a92,rgba(63,106,146,0)),
  linear-gradient(135deg,#4f7aa3,#a9c6dd 35%,#e6eaee 60%,#5e84ab)}
/* testimonials */
.testimonials{position:absolute;left:0;top:1997px;width:1200px;height:373px;background:var(--purple-soft)}
.testimonials .section-title{top:36px;color:var(--purple-deep)}
.quote{position:absolute;left:148px;top:108px;width:950px;font-style:italic;font-size:14px;line-height:1.75;color:var(--ink);text-align:center}
.quote-mark{position:absolute;left:110px;top:94px;font-size:60px;color:var(--green);font-family:Georgia,serif;line-height:1}
.avatar{position:absolute;left:565px;top:228px;width:68px;height:68px;border-radius:50%;background:radial-gradient(circle at 50% 40%,#e6e2dc,#a9a49c 70%,#8e8a83);border:3px solid var(--white)}
.client{position:absolute;left:0;width:1200px;top:306px;text-align:center;font-size:14px;font-style:italic;color:var(--ink)}
.slider-arrow{position:absolute;top:125px}
/* blog */
.blog .section-title{top:2436px;color:var(--purple-deep)}
.post{position:absolute;top:2514px;width:488px}
.post-image{width:488px;height:249px}
.post-date{position:absolute;right:20px;top:199px;width:56px;text-align:center;color:var(--white);font-family:"Oswald",sans-serif}
.post-date b{display:block;background:var(--green);font-size:22px;font-weight:500;height:46px;line-height:46px}
.post-date span{display:block;background:var(--purple-deep);font-size:15px;height:36px;line-height:36px}
.post h3{font-size:24px;font-weight:700;margin-top:40px;color:var(--ink)}
.post p{font-size:13.5px;line-height:1.65;color:var(--muted);margin-top:18px}
.btn-green{display:inline-block;margin-top:28px;background:var(--green);color:var(--white);font-size:14px;padding:9px 12px}
/* ratings */
.rating{position:absolute;top:3088px;height:233px;border:2px solid var(--purple);display:flex;flex-direction:column;align-items:center;justify-content:center;gap:16px}
.rating .name{font-size:48px;font-weight:700;color:var(--purple-deep)}
/* partners */
.partners{position:absolute;left:0;top:3386px;width:1200px;height:285px;background:var(--grey-band)}
.partners .section-title{top:42px;color:var(--purple-deep)}
.partner{position:absolute;top:117px;width:176px;height:122px;background:var(--white);display:flex;align-items:center;justify-content:center}
.partner i{display:block;width:110px;height:40px;border-radius:6px;background:#dcd4e6}
/* footer */
.site-footer{position:absolute;left:0;top:3671px;width:1200px;height:344px;background:var(--footer);color:#d8d8d8}
.footer-brand{position:absolute;left:84px;top:50px;display:flex;align-items:center;gap:10px}
.footer-brand .brand-mark{width:52px;height:52px;border-color:var(--white)}
.footer-brand .brand-name{color:var(--white);font-size:17px}
.footer-brand .brand-name small{color:#cfcfcf;font-size:12px}
.footer-about{position:absolute;left:84px;top:134px;width:720px;font-size:13px;line-height:1.7}
.tweets-title{position:absolute;left:876px;top:40px;font-size:26px;font-weight:400;color:var(--white)}
.tweet{position:absolute;left:876px;width:240px;height:96px;background:var(--footer-deep);padding:10px 12px;font-size:11px;color:#cfcfcf}
.tweet b{color:var(--white);display:block;font-size:12px}
.tweet .meta{display:flex;justify-content:space-between;margin-top:14px;color:#999}
.copyright{position:absolute;left:0;top:4015px;width:1200px;height:48px;background:var(--footer-deep);color:#9a9a9a;font-size:12px;padding:0 84px;display:flex;align-items:center;justify-content:space-between}
</style>
</head>
<body>

<svg class="icon-defs" aria-hidden="true">
  <defs>
    <path id="star" d="M18 2l4.7 10 10.8 1.2-8 7.3 2.3 10.6L18 25.8 8.2 31.1l2.3-10.6-8-7.3L13.3 12z"/>
    <g id="ico-spine" fill="none" stroke="#fff" stroke-width="2.5" stroke-linecap="round">
      <rect x="18" y="6" width="12" height="5" rx="2"/><rect x="17" y="14" width="14" height="5" rx="2"/><rect x="16" y="22" width="16" height="5" rx="2"/><rect x="17" y="30" width="14" height="5" rx="2"/><rect x="18" y="38" width="12" height="5" rx="2"/>
    </g>
    <g id="ico-dumbbell" fill="none" stroke="#fff" stroke-width="2.5" stroke-linejoin="round">
      <path d="M14 24h20"/><rect x="8" y="15" width="6" height="18" rx="1.5"/><rect x="34" y="15" width="6" height="18" rx="1.5"/><rect x="4" y="19" width="4" height="10" rx="1"/><rect x="40" y="19" width="4" height="10" rx="1"/>
    </g>
    <g id="ico-heart" fill="none" stroke="#fff" stroke-width="2.5" stroke-linejoin="round" stroke-linecap="round">
      <path d="M24 40C10 30 5 21 9 14c4-6 11-5 15 2 4-7 11-8 15-2 4 7-1 16-15 26z"/><path d="M11 25h7l3-6 5 11 3-5h8"/>
    </g>
    <g id="ico-care" fill="none" stroke="#fff" stroke-width="2.5" stroke-linejoin="round" stroke-linecap="round">
      <path d="M24 5c4 7 7 11 7 15a7 7 0 0 1-14 0c0-4 3-8 7-15z"/><path d="M5 36l7-4h9l4 3h11l6-4M5 42h32l7-5"/>
    </g>
  </defs>
</svg>

<header class="site-header">
  <div class="brand">
    <div class="brand-mark"></div>
    <div class="brand-name">Thornleigh Vitality Centre<small>Call 555-010-0199</small></div>
  </div>
  <div class="topbar">
    <span><svg width="11" height="11" viewBox="0 0 24 24"><path d="M6.6 10.8a15 15 0 0 0 6.6 6.6l2.2-2.2c.3-.3.7-.4 1-.2 1.1.4 2.3.6 3.6.6.6 0 1 .4 1 1V20c0 .6-.4 1-1 1A17 17 0 0 1 3 4c0-.6.4-1 1-1h3.5c.6 0 1 .4 1 1 0 1.3.2 2.5.6 3.6.1.3 0 .7-.2 1z"/></svg>555-010-0199</span>
    <span><svg width="11" height="11" viewBox="0 0 24 24"><rect x="3" y="5" width="18" height="14" rx="2"/></svg>555-010-0199</span>
    <span><svg width="10" height="12" viewBox="0 0 24 28"><path d="M12 0a10 10 0 0 0-10 10c0 7 10 18 10 18s10-11 10-18A10 10 0 0 0 12 0zm0 14a4 4 0 1 1 0-8 4 4 0 0 1 0 8z"/></svg>48 Larkfield Avenue, Suite 210, Toronto, Ontario, M0X 2Z9</span>
    <span class="social"><i></i><i></i><i></i></span>
  </div>
  <div class="topbar-rule"></div>
  <nav class="main-nav">
    <span>Home</span><span>Fees and Services</span><span>Our Staff</span><span>News and Updates</span><span>Corporate Wellness</span><span>Forms</span><span>Contact</span>
  </nav>
</header>

<section class="hero">
  <div class="hero-photo" role="img" aria-label="Therapist treating a client's leg on a treatment table in a bright clinic"></div>
  <div class="hero-shade"></div>
  <svg class="hero-arrow" style="left:22px" width="20" height="50" viewBox="0 0 20 50"><path d="M16 2 4 25l12 23" fill="none" stroke="#fff" stroke-width="2"/></svg>
  <svg class="hero-arrow" style="right:22px" width="20" height="50" viewBox="0 0 20 50"><path d="M4 2l12 23L4 48" fill="none" stroke="#fff" stroke-width="2"/></svg>
  <div class="hero-kicker">WELCOME TO</div>
  <h1 class="hero-title">THORNLEIGH VITALITY CENTRE</h1>
  <div class="btn-outline-light">BOOK AN APPOINTMENT
    <svg width="14" height="14" viewBox="0 0 14 14"><circle cx="7" cy="7" r="6" fill="none" stroke="#fff" stroke-width="1.5"/><path d="M6 4l3 3-3 3" fill="none" stroke="#fff" stroke-width="1.5"/></svg>
  </div>
</section>

<section class="location">
  <h2>Visit our new location</h2>
  <p style="left:84px">We are open for business at 7:30 am. Open 7 days a week!</p>
  <p style="left:626px">Ask one of our associates about our Referral Reward Program!</p>
  <div class="btn-outline">SEE MAP
    <svg width="12" height="12" viewBox="0 0 14 14"><circle cx="7" cy="7" r="6" fill="none" stroke="#886aae" stroke-width="1.5"/><path d="M6 4l3 3-3 3" fill="none" stroke="#886aae" stroke-width="1.5"/></svg>
  </div>
</section>

<section class="services">
  <div class="services-photo" role="img" aria-label="Faint photo of a therapist adjusting a client's shoulder"></div>
  <div class="services-tint"></div>
  <h2 class="section-title">OUR SERVICES</h2>
  <div class="service" style="left:70px;top:128px"><div class="service-icon"><div class="service-ring"><svg viewBox="0 0 48 48" role="img" aria-label="Chiropractic"><use href="#ico-spine"/></svg></div></div>Chiropractic</div>
  <div class="service" style="left:285px;top:128px"><div class="service-icon"><div class="service-ring"><svg viewBox="0 0 48 48" role="img" aria-label="Physiotherapy"><use href="#ico-dumbbell"/></svg></div></div>Physiotherapy</div>
  <div class="service" style="left:500px;top:128px"><div class="service-icon"><div class="service-ring"><svg viewBox="0 0 48 48" role="img" aria-label="Active rehabilitation"><use href="#ico-heart"/></svg></div></div>Active Rehabilitation</div>
  <div class="service" style="left:710px;top:128px"><div class="service-icon"><div class="service-ring"><svg viewBox="0 0 48 48" role="img" aria-label="Massage therapy"><use href="#ico-care"/></svg></div></div>Massage Therapy</div>
  <div class="service" style="left:930px;top:128px"><div class="service-icon"><div class="service-ring"><svg viewBox="0 0 48 48" role="img" aria-label="Physiotherapy"><use href="#ico-dumbbell"/></svg></div></div>Physiotherapy</div>
  <div class="service" style="left:285px;top:322px"><div class="service-icon"><div class="service-ring"><svg viewBox="0 0 48 48" role="img" aria-label="Physiotherapy"><use href="#ico-dumbbell"/></svg></div></div>Physiotherapy</div>
  <div class="service" style="left:500px;top:322px"><div class="service-icon"><div class="service-ring"><svg viewBox="0 0 48 48" role="img" aria-label="Active rehabilitation"><use href="#ico-heart"/></svg></div></div>Active Rehabilitation</div>
  <div class="service" style="left:710px;top:322px"><div class="service-icon"><div class="service-ring"><svg viewBox="0 0 48 48" role="img" aria-label="Massage therapy"><use href="#ico-care"/></svg></div></div>Massage Therapy</div>
</section>

<section class="about">
  <div class="about-text">
    <h3>Our Centre is committed to helping improve and extend the lives of as many people as possible in our community.</h3>
    <p class="sub">Come and join our Family and start changing your life today.</p>
    <h4>Planning a wellness fair? We can help!</h4>
    <p>Contact us at<br><a>info@thornleighvitality.example</a> for more details</p>
  </div>
  <div class="video" role="img" aria-label="Video still of a practitioner explaining a spine model to a patient">
    <svg width="60" height="70" viewBox="0 0 60 70"><path d="M6 4l48 31L6 66z" fill="none" stroke="#fff" stroke-width="4"/></svg>
  </div>
</section>

<section class="testimonials">
  <h2 class="section-title">WHAT OUR CLIENTS SAY</h2>
  <svg class="slider-arrow" style="left:62px" width="18" height="46" viewBox="0 0 18 46"><path d="M15 2 3 23l12 21" fill="none" stroke="#555" stroke-width="2"/></svg>
  <svg class="slider-arrow" style="right:62px" width="18" height="46" viewBox="0 0 18 46"><path d="M3 2l12 21L3 44" fill="none" stroke="#555" stroke-width="2"/></svg>
  <div class="quote-mark">&ldquo;</div>
  <p class="quote">I attended your clinic recently and was surprised. I am 68 years old and never before was I received so warmly.&nbsp; I believe that natural medicine is the best medicine for all of us. It has fewer and more benign side-effects than those created in labs. Your clinic I dream will be the future of health care. My regret is that most patients are misled by the medical and pharmaceutical powers that be to sway their minds to traditional methods of treating their conditions. I wish all of you&nbsp; well in your endeavors.&nbsp; <span style="color:var(--green-dark)">Regards Jack</span></p>
  <div class="avatar" role="img" aria-label="Client portrait"></div>
  <div class="client">Dr. Halvern</div>
</section>

<section class="blog">
  <h2 class="section-title">OUR BLOG</h2>
  <article class="post" style="left:84px">
    <div class="post-image" role="img" aria-label="Therapist stretching a client's leg beside a green plant" style="background:
      radial-gradient(ellipse 120px 140px at 430px 90px,#8fb04e,rgba(143,176,78,0)),
      radial-gradient(ellipse 200px 70px at 230px 180px,#3c3f46,rgba(60,63,70,0)),
      radial-gradient(ellipse 160px 80px at 180px 90px,#d9ad8e,rgba(217,173,142,0)),
      linear-gradient(120deg,#f1f2ee,#e4e7df 50%,#f6f6f3)"></div>
    <div class="post-date"><b>04</b><span>JUL</span></div>
    <h3>Best Business solution</h3>
    <p>Lorem Ipsum is simply dummy text of the printing and typesetting industry. Lorem Ipsum has been the industry's standard dummy text ever since the 1500s, when an unknown printer took a galley of type and scrambled it to make a type specimen book. It has survived not only five centuries, but also the leap into electronic typesetting, remaining</p>
    <span class="btn-green">Learn more</span>
  </article>
  <article class="post" style="left:626px">
    <div class="post-image" role="img" aria-label="Client relaxing during a back massage" style="background:
      radial-gradient(ellipse 240px 90px at 300px 170px,#d39f7e,rgba(211,159,126,0)),
      radial-gradient(ellipse 110px 90px at 140px 90px,#c98e6c,rgba(201,142,108,0)),
      radial-gradient(ellipse 160px 70px at 100px 220px,#ffffff,rgba(255,255,255,0)),
      linear-gradient(120deg,#f4f1ed,#efe6de 50%,#f8f6f3)"></div>
    <div class="post-date"><b>04</b><span>JUL</span></div>
    <h3>Best Business Service</h3>
    <p>Lorem Ipsum is simply dummy text of the printing and typesetting industry. Lorem Ipsum has been the industry's standard dummy text ever since the 1500s, when an unknown printer took a galley of type and scrambled it to make a type specimen book. It has survived not only five centuries, but also the leap into electronic typesetting, remaining</p>
    <span class="btn-green">Learn more</span>
  </article>
</section>

<section class="ratings">
  <div class="rating" style="left:84px;width:328px"><span class="name">Quorva</span>
    <svg width="200" height="36" viewBox="0 0 200 36" fill="#acd036"><use href="#star"/><use href="#star" x="41"/><use href="#star" x="82"/><use href="#star" x="123"/><use href="#star" x="164"/></svg>
  </div>
  <div class="rating" style="left:439px;width:325px"><span class="name">Zintrel</span>
    <svg width="200" height="36" viewBox="0 0 200 36" fill="#acd036"><use href="#star"/><use href="#star" x="41"/><use href="#star" x="82"/><use href="#star" x="123"/><use href="#star" x="164"/></svg>
  </div>
  <div class="rating" style="left:788px;width:325px"><span class="name">PostMaz</span>
    <svg width="200" height="36" viewBox="0 0 200 36" fill="#acd036"><use href="#star"/><use href="#star" x="41"/><use href="#star" x="82"/><use href="#star" x="123"/><use href="#star" x="164"/></svg>
  </div>
</section>

<section class="partners">
  <h2 class="section-title">OUR PARTNERS</h2>
  <div class="partner" style="left:88px" role="img" aria-label="Partner badge"><i></i></div>
  <div class="partner" style="left:298px" role="img" aria-label="Partner badge"><i></i></div>
  <div class="partner" style="left:510px" role="img" aria-label="Partner badge"><i></i></div>
  <div class="partner" style="left:723px" role="img" aria-label="Partner badge"><i></i></div>
  <div class="partner" style="left:936px" role="img" aria-label="Partner badge"><i></i></div>
</section>

<footer class="site-footer">
  <div class="footer-brand">
    <div class="brand-mark"></div>
    <div class="brand-name">Thornleigh Vitality Centre<small>Call 555-010-0199</small></div>
  </div>
  <p class="footer-about">Established in 1989 the Thornleigh Vitality Centre has become one of Canada's leaders in providing quality care and innovative wellness programs for the community. The founder and director Dr. Owen Calder's vision has come to life with over 30 practitioners providing a multitude of different services under one roof. Some of the services include Chiropractic, Physiotherapy, Athletic Therapy, Naturopathy, Massage Therapy, Acupuncture and Personal Training. The Thornleigh Vitality Centre has a complete Pilates studio on its premises. We also offer many wellness seminars free of cost to the public. Our Centre is committed to helping improve and extend the lives of as many people as possible in our community. Come and join our Family and start changing your life today.</p>
  <h3 class="tweets-title">Our Tweets</h3>
  <div class="tweet" style="top:92px"><b>Thornleigh Vitality</b>@ThornleighVital<br>New pilates classes start Monday<div class="meta"><span>♡ ↻</span><span>Aug 30, 2017</span></div></div>
  <div class="tweet" style="top:205px"><b>Thornleigh Vitality</b>@ThornleighVital<br>Book your posture check today<div class="meta"><span>♡ ↻</span><span>Aug 30, 2017</span></div></div>
</footer>
<div class="copyright"><span>Copyright 2017.</span><span class="social"><i></i><i></i></span></div>

</body>
</html>
```